Nobody Left the Lantern Burning - Tom Halvery - CD Cover Design Project

Single Cover for CD & Online media e.g. Tunebox Graphics
The first song release from Tom Halvery will be the track 'Nobody Left the Lantern Burning'.
For the release the single requires artwork that is eye catching, seriously professional & meets the requirements of Disc Sprout, Tunebox and also a physical copy on CD.
Track listings for CD will be:
1. Nobody Left the Lantern Burning
2. Nobody Left the Lantern Burning - Instrumental
see details in this link:
http://members.discsprout-example.com/faq.aspx
http://selfmadesound.discsprout-example.com/2009/11/avoid-album-art-atrocities/
http://answers.quorvex-example.com/question/index?qid=20111015141433AAdDTmH
Any advice on this would be greatly appreciated,
I would also like the two logo's I have uploaded to be used,
one is the Tom Halvery logo and the other is for Milbrook & Tandy Records logo (please remove the R and replace with a C for copyright.)
There are four high res photo shopped pictures of Tom Halvery and another zip file of many others, it would be nice to include one of these maybe on the 2nd page or back of the CD. Please don't use them as the front cover.
I imagine an Art Deco illustration but please listen to the track and let it inspire you.
Good Luck
Updates
I don't feel this is what I'm looking for, the design needs to refelct a broken heart without being a picture of a broken heart
Reason: No design has been what we are after so far so the deadline has been extended and the budget increased.

```html
<!DOCTYPE html>
<html lang="en">
<head>
<meta charset="utf-8">
<title>Nobody Left the Lantern Burning – Tom Halvery</title>
<link rel="stylesheet" href="https://fonts.googleapis.com/css2?family=Inter:wght@800&family=Open+Sans:wght@400&display=swap">
<style>
  :root {
    --ink-dark: #141414;
    --ink-light: #d6d6d6;
    --title-white: #f4f4f4;
    --texture-deep: #1e1e1e;
    --texture-mid: #4a4a4a;
    --texture-pale: #9a9a9a;
  }
  html, body {
    margin: 0;
    padding: 0;
    overflow: hidden;
    background: #ffffff;
  }
  .cover {
    position: relative;
    width: 1200px;
    height: 1200px;
    overflow: hidden;
  }
  .cover-art {
    position: absolute;
    inset: 0;
    display: block;
  }
  .song-title {
    font-family: "Open Sans", sans-serif;
    font-weight: 400;
    fill: var(--title-white);
  }
  .artist-first {
    font-family: "Inter", sans-serif;
    font-weight: 800;
    fill: var(--ink-dark);
  }
  .artist-last {
    font-family: "Inter", sans-serif;
    font-weight: 800;
    fill: var(--ink-light);
  }
</style>
</head>
<body>
<main class="cover">
  <svg class="cover-art" width="1200" height="1200" viewBox="0 0 1200 1200" xmlns="http://www.w3.org/2000/svg">
    <defs>
      <linearGradient id="texture-base" x1="0" y1="0" x2="1" y2="1">
        <stop offset="0" stop-color="var(--texture-mid)"/>
        <stop offset="0.45" stop-color="var(--texture-deep)"/>
        <stop offset="1" stop-color="var(--texture-mid)"/>
      </linearGradient>
      <radialGradient id="texture-glow-left" cx="0.12" cy="0.7" r="0.45">
        <stop offset="0" stop-color="var(--texture-pale)" stop-opacity="0.85"/>
        <stop offset="1" stop-color="var(--texture-pale)" stop-opacity="0"/>
      </radialGradient>
      <radialGradient id="texture-glow-top" cx="0.35" cy="0.05" r="0.4">
        <stop offset="0" stop-color="var(--texture-pale)" stop-opacity="0.5"/>
        <stop offset="1" stop-color="var(--texture-pale)" stop-opacity="0"/>
      </radialGradient>
      <radialGradient id="texture-glow-right" cx="0.9" cy="0.75" r="0.35">
        <stop offset="0" stop-color="var(--texture-pale)" stop-opacity="0.55"/>
        <stop offset="1" stop-color="var(--texture-pale)" stop-opacity="0"/>
      </radialGradient>
    </defs>

    <g class="grunge-texture" role="img" aria-label="Distressed grey grunge texture with scratched, stained surface">
      <rect width="1200" height="1200" fill="url(#texture-base)"/>
      <rect width="1200" height="1200" fill="url(#texture-glow-left)"/>
      <rect width="1200" height="1200" fill="url(#texture-glow-top)"/>
      <rect width="1200" height="1200" fill="url(#texture-glow-right)"/>
    </g>

    <text class="song-title" x="600" y="128" font-size="47" text-anchor="middle"
          textLength="1020" lengthAdjust="spacingAndGlyphs">NOBODY LEFT THE LANTERN BURNING</text>

    <text class="artist-first" x="0" y="900" font-size="462"
          textLength="1200" lengthAdjust="spacingAndGlyphs">TOM</text>

    <text class="artist-last" x="0" y="1226" font-size="347"
          textLength="1200" lengthAdjust="spacingAndGlyphs">HALVERY</text>
  </svg>
</main>
</body>
</html>
```